Ranked amongst the Best Colleges and Programs

the size of the ad is Full Page, with bleed*
8”x 10.75" plus 0.25" bleed'
you have two choices for the tagline .. please chose what ever you think will allow you to make a better ad.
The instructions on the brief are in red
I am looking for a hight quality modern ad to place in local weekly publications that will stand out .
I would like a ad that people will look at and say i would like to see what this ad is all about.
I apprecate creative work.
the ad should not be very crowded and the text should be able to be read.
if you decide to use people in the ad .. (you don't have to ) then it should be a male dressed in white shirt in and sports jacket.. or if you would like you can use a vector and then use male or female people.
please leave one inch on the bottom for the footer

Target Market(s)

potential middle class students from 23-35 years of age

Industry/Entity Type

education

Requirements
Must have
• .the " 98% employment rate" should stand out in the ad.. but should not be the main part of the ad
Nice to have
• creative
Should not have
• Should not be a very busy or crowded ad.. i prefer pictures of men but should be .. in a business suit .. that looks professional- white shirt

```html
<!DOCTYPE html>
<html lang="en">
<head>
<meta charset="utf-8">
<title>NVU Masters of Accounting – Ad</title>
<link rel="stylesheet" href="https://fonts.googleapis.com/css2?family=Oswald:wght@500;600&family=Poppins:wght@400;600;700;800&display=swap">
<style>
  :root {
    --navy: #0a1140;
    --navy-panel: #0b2a66;
    --blue: #0a4fc0;
    --blue-bright: #1259d6;
    --white: #ffffff;
    --page-bg: #eceef1;
    --badge-cream: #fbf5e8;
    --badge-gold: #e3b664;
    --divider: #c9ccd4;
  }
  html, body { margin: 0; padding: 0; }
  body {
    width: 1200px; height: 2920px; overflow: hidden;
    background: var(--page-bg);
    position: relative;
    font-family: "Poppins", sans-serif;
  }
  .ad {
    position: absolute; left: 50px; top: 728px;
    width: 1100px; height: 1463px;
    background: var(--white);
    overflow: hidden;
  }
  .ad > * { z-index: 2; }
  .headline {
    position: absolute; left: 0; right: 0; top: 40px;
    margin: 0; text-align: center;
    font-family: "Poppins", sans-serif; font-weight: 800;
    font-size: 82px; line-height: 79px; letter-spacing: -1px;
    color: var(--navy);
  }
  .headline .accent { color: var(--blue); display: block; }
  .headline .lead { display: block; }

  .program-bar {
    position: absolute; left: 70px; top: 399px;
    width: 820px; height: 86px;
    background: var(--navy);
    border-radius: 14px 0 0 14px;
    display: flex; align-items: center;
    font-family: "Oswald", sans-serif; font-weight: 600;
    font-size: 50px; color: var(--white); letter-spacing: 0.5px;
    white-space: nowrap;
  }
  .program-bar .school {
    background: var(--blue); height: 100%;
    display: flex; align-items: center;
    padding: 0 8px 0 18px; border-radius: 14px 0 0 14px;
  }
  .program-bar .program { padding-left: 10px; }

  .ranked-label {
    position: absolute; left: 70px; top: 518px; margin: 0;
    font-weight: 600; font-size: 44px; color: var(--navy);
  }
  .rank-card {
    position: absolute; top: 589px; height: 203px;
    background: var(--navy-panel);
    border: 3px solid #9aa3b8; border-radius: 14px;
    box-sizing: border-box;
    color: var(--white); text-align: center;
    font-weight: 600; font-size: 30px; line-height: 31px;
    padding-top: 18px;
  }
  .rank-card.colleges { left: 70px; width: 319px; }
  .rank-card.masters { left: 398px; width: 323px; border-color: var(--blue-bright); }
  .rank-card .badge {
    position: absolute; left: 28px; right: 28px; bottom: 0;
    height: 110px; border-radius: 12px 12px 0 0;
  }
  .rank-card.colleges .badge { background: var(--blue-bright); }
  .rank-card.masters .badge {
    left: 16px; right: 16px; bottom: 14px; height: 92px;
    border-radius: 6px; background: var(--badge-cream);
    border: 2px solid var(--badge-gold);
  }

  .divider {
    position: absolute; left: 100px; top: 826px; width: 540px;
    border-top: 2px dotted var(--divider);
  }
  .stat {
    position: absolute; left: 70px; top: 842px;
    display: flex; align-items: flex-start;
  }
  .stat .figure {
    font-weight: 600; font-size: 140px; line-height: 140px;
    color: var(--blue); letter-spacing: -2px;
  }
  .stat .figure sup { font-size: 68px; vertical-align: top; position: relative; top: 6px; }
  .stat .label {
    font-family: "Oswald", sans-serif; font-weight: 600;
    font-size: 50px; line-height: 50px; color: var(--navy);
    margin: 22px 0 0 14px;
  }

  .ad > .photo {
    position: absolute; left: 660px; top: 380px;
    width: 440px; height: 901px;
    background: linear-gradient(180deg, #e9eaee 0%, #f3f3f5 45%, #d9dbe0 100%);
    border-radius: 200px 200px 0 0;
    z-index: 1;
  }

  .grads-panel {
    position: absolute; left: 0; top: 1005px; width: 641px; height: 276px;
    background: linear-gradient(90deg, var(--navy-panel), #0a2c72);
    color: var(--white);
  }
  .grads-panel .rule {
    position: absolute; left: 72px; top: 36px; width: 7px; height: 208px;
    background: var(--blue-bright);
  }
  .grads-panel h2 {
    position: absolute; left: 101px; top: 22px; margin: 0;
    font-weight: 600; font-size: 37px;
  }
  .grads-panel p {
    position: absolute; left: 101px; top: 78px; margin: 0; width: 520px;
    font-weight: 400; font-size: 28px; line-height: 34.5px;
  }
  .base-stripe {
    position: absolute; left: 0; top: 1281px; width: 1100px; height: 13px;
    background: var(--blue-bright);
  }
</style>
</head>
<body>
  <main class="ad">
    <div class="photo" role="img" aria-label="Smiling young businessman in glasses, white shirt and dark tie, gesturing toward the text"></div>

    <h1 class="headline">
      <span class="lead">A SMALL</span>
      <span class="lead">INVESTMENT TODAY,</span>
      <span class="accent">A BIG DIFFERENCE</span>
      <span class="accent">TOMORROW.</span>
    </h1>

    <div class="program-bar">
      <span class="school">NVU-</span>
      <span class="program">MASTERS OF ACCOUNTING</span>
    </div>

    <h3 class="ranked-label">RANKED AMONGST:</h3>

    <div class="rank-card colleges">
      BEST<br>COLLEGES
      <div class="badge" role="img" aria-label="College ranking badge"></div>
    </div>
    <div class="rank-card masters">
      BEST MASTERS IN<br>ACCOUNTING
      <div class="badge" role="img" aria-label="Masters ranking badge"></div>
    </div>

    <div class="divider"></div>

    <div class="stat">
      <span class="figure">98<sup>%</sup></span>
      <span class="label">EMPLOYMENT<br>RATE</span>
    </div>

    <section class="grads-panel">
      <span class="rule"></span>
      <h2>NVU graduates</h2>
      <p>have gone on to work in various high-quality jobs in top firms, earning impressive six-figure salaries as well as opening successful businesses.</p>
    </section>

    <div class="base-stripe"></div>
  </main>
</body>
</html>
```